Brindle Gateworks garage door installation service and repairs

I need a business card design for my company that is called Brindle Gateworks, I install, service, repair and automate garaged doors.
I want my card to look simple and neat but I also want the information such as contact number, email address and website to be clear and noticeable. I would love a simple logo if possible, I would like to see the color blue in the card but not overpowering.

Industry/Entity Type

Garage

```html
<!DOCTYPE html>
<html lang="en">
<head>
<meta charset="utf-8">
<title>Brindle Gateworks – Business Card</title>
<link rel="stylesheet" href="https://fonts.googleapis.com/css2?family=Exo+2:wght@400;600;800&display=swap">
<style>
  :root{
    --backdrop:#2b2e30;
    --card:#ffffff;
    --card-shade:#eef0f1;
    --teal:#2a97b3;
    --teal-bar:#56b8cc;
    --teal-bar-end:#7fc9d8;
    --teal-icon:#3cc6dc;
    --rule:#c9d0d3;
    --ink-light:#ffffff;
  }
  *{margin:0;padding:0;box-sizing:border-box}
  html,body{width:1200px;height:899px;overflow:hidden}
  body{
    background:var(--backdrop);
    font-family:"Exo 2",sans-serif;
    position:relative;
  }
  .business-card{
    position:absolute;
    left:210px;top:227px;
    width:780px;height:446px;
    background:linear-gradient(160deg,var(--card) 0%,var(--card) 55%,var(--card-shade) 100%);
    box-shadow:0 10px 30px rgba(0,0,0,.35);
  }
  .brand-name{
    position:absolute;
    left:68px;top:128px;
    color:var(--teal);
    font-weight:800;
    font-size:42px;
    line-height:1.05;
    letter-spacing:1px;
    text-transform:uppercase;
  }
  .contact-list{
    position:absolute;
    left:430px;top:110px;
    width:350px;
    list-style:none;
  }
  .contact-item{
    display:flex;align-items:center;
    height:24px;
    margin-bottom:20px;
    background:linear-gradient(90deg,var(--teal-bar),var(--teal-bar-end));
    color:var(--ink-light);
    font-size:16px;
    letter-spacing:.5px;
  }
  .contact-item:nth-child(2){width:300px}
  .contact-item:nth-child(3){width:300px}
  .contact-icon{
    width:24px;height:24px;
    background:var(--teal-icon);
    display:flex;align-items:center;justify-content:center;
    margin-right:16px;
    flex:none;
  }
  .contact-icon svg{width:14px;height:14px}
  .divider{
    position:absolute;
    left:36px;top:288px;
    width:644px;height:2px;
    background:var(--rule);
  }
  .tagline{
    position:absolute;
    left:36px;top:302px;
    color:var(--teal);
    font-size:17.5px;
    font-weight:400;
    letter-spacing:1.6px;
    text-transform:uppercase;
  }
</style>
</head>
<body>
  <article class="business-card">
    <h1 class="brand-name">Brindle<br>Gateworks</h1>

    <ul class="contact-list">
      <li class="contact-item">
        <span class="contact-icon">
          <svg viewBox="0 0 24 24" fill="none" stroke="#fff" stroke-width="2.2" stroke-linejoin="round"><path d="M6 3h4l1.5 5-2.5 1.5a11 11 0 0 0 5.5 5.5L16 12.5l5 1.5v4a2 2 0 0 1-2 2A17 17 0 0 1 4 5a2 2 0 0 1 2-2z"/></svg>
        </span>
        +00 9876543210
      </li>
      <li class="contact-item">
        <span class="contact-icon">
          <svg viewBox="0 0 24 24" fill="none" stroke="#fff" stroke-width="2.2" stroke-linejoin="round"><rect x="3" y="6" width="18" height="12"/><path d="M3 6l9 7 9-7"/></svg>
        </span>
        hello@brindlegateworks.com
      </li>
      <li class="contact-item">
        <span class="contact-icon">
          <svg viewBox="0 0 24 24" fill="none" stroke="#fff" stroke-width="2"><circle cx="12" cy="12" r="9"/><ellipse cx="12" cy="12" rx="4" ry="9"/><path d="M3 12h18"/></svg>
        </span>
        www.brindlegateworks.com
      </li>
    </ul>

    <div class="divider"></div>
    <p class="tagline">I install, service, repair and automate garaged doors.</p>
  </article>
</body>
</html>
```